Modern Business Card For A Digital Advertising Company

I'll be print on the Tarn Prints Velour paper http://us.tarnprints.example/products/velour/business-cards.html
Need's to be modern and use the color palette of the logo or gray scales. I think integrating the pixelation of the logo in to the card and having it wrap from one side to the other could be interesting. My company provides ad operations, web development, and number of other services to websites around the world. You can see my website at http://www.pixelharbor.example
Contact info on the card needs to have
Dana Welloby
President
p.555.318.4406
dana@pixelharbor.example
http://www.pixelharbor.example
Doesn't necessarily need to be in that order
Target Market(s)
Website owners
Industry/Entity Type
Business
Look and feel

```html
<!DOCTYPE html>
<html lang="en">
<head>
<meta charset="utf-8">
<title>Pixel Harbor – Business Card</title>
<link rel="stylesheet" href="https://fonts.googleapis.com/css2?family=Arimo:wght@400;700&display=swap">
<style>
  :root {
    --backdrop: #2b2b2b;
    --card: #ffffff;
    --brand-green: #7dc242;
    --ink: #333333;
    --pixel-grey: #d4d4d4;
  }
  html, body {
    margin: 0;
    padding: 0;
    width: 1200px;
    height: 1000px;
    overflow: hidden;
    background: var(--backdrop);
    font-family: "Arimo", Arial, sans-serif;
  }
  .canvas {
    position: relative;
    width: 1200px;
    height: 1000px;
  }
  .business-card {
    position: absolute;
    left: 395px;
    top: 142px;
    width: 410px;
    height: 715px;
    background: var(--card);
    border-top-right-radius: 70px;
    box-shadow: 0 6px 18px rgba(0,0,0,.35);
  }
  .brand {
    position: absolute;
    left: 142px;
    top: 150px;
    display: flex;
    align-items: flex-start;
    gap: 12px;
  }
  .brand-square {
    width: 22px;
    height: 22px;
    background: var(--brand-green);
    margin-top: 8px;
  }
  .brand-name {
    margin: 0;
    color: var(--brand-green);
    font-weight: 700;
    font-size: 44px;
    line-height: 44px;
    letter-spacing: 2px;
  }
  .pixel-cluster {
    position: absolute;
    display: block;
  }
  .pixel-cluster--top { left: 4px; top: 84px; }
  .pixel-cluster--bottom { left: 316px; top: 587px; }
  .holder {
    position: absolute;
    left: 142px;
    top: 338px;
  }
  .holder-name {
    margin: 0;
    color: var(--ink);
    font-weight: 700;
    font-size: 24px;
    line-height: 30px;
  }
  .holder-title {
    margin: 4px 0 0;
    color: var(--brand-green);
    font-weight: 700;
    font-size: 24px;
    line-height: 30px;
  }
  .website {
    position: absolute;
    left: 24px;
    top: 674px;
    transform: rotate(-90deg);
    transform-origin: left top;
    color: var(--ink);
    font-size: 15px;
    letter-spacing: 5px;
    white-space: nowrap;
  }
  .contact {
    position: absolute;
    left: 103px;
    top: 636px;
    font-size: 23px;
    line-height: 34px;
  }
  .contact-phone { color: var(--ink); font-weight: 700; }
  .contact-phone .label { font-weight: 400; }
  .contact-email { color: var(--brand-green); }
</style>
</head>
<body>
<main class="canvas">
  <article class="business-card">
    <div class="brand">
      <span class="brand-square"></span>
      <h1 class="brand-name">PIXEL<br>HARBOR</h1>
    </div>

    <svg class="pixel-cluster pixel-cluster--top" width="95" height="54" role="img" aria-label="Grey pixel cluster pattern">
      <rect width="95" height="54" fill="var(--pixel-grey)" opacity=".6"/>
    </svg>
    <svg class="pixel-cluster pixel-cluster--bottom" width="58" height="58" role="img" aria-label="Grey pixel cluster pattern">
      <rect width="58" height="58" fill="var(--pixel-grey)" opacity=".6"/>
    </svg>

    <div class="holder">
      <p class="holder-name">Dana Welloby</p>
      <p class="holder-title">President</p>
    </div>

    <div class="website">www.pixelharbor.example</div>

    <div class="contact">
      <div class="contact-phone"><span class="label">P.</span> 555.318.4406</div>
      <div class="contact-email">dana@pixelharbor.example</div>
    </div>
  </article>
</main>
</body>
</html>
```